Bref créative
Letterhead, envelope, business card
Sunny Harbor Snackworks, LLC
Bright & Fun-filled
Daniel T. Whitcombe
Partner
4870 Lakeview Court East
Morganville, NJ 07751
dwhitcombe@sunnyharborsnackworks.com
sunnyharborsnackworks.com

```html
<!DOCTYPE html>
<html lang="en">
<head>
<meta charset="utf-8">
<title>Sunny Harbor Snackworks – Stationery</title>
<link href="https://fonts.googleapis.com/css2?family=Open+Sans:wght@400;600;800&display=swap" rel="stylesheet">
<style>
:root{
  --bg:#e6e8ec;
  --paper:#ffffff;
  --navy:#1d3f8f;
  --blue:#2a6fc9;
  --sky:#4aa3df;
  --red:#d6262e;
  --ink:#33415c;
  --line:#c9d3e3;
}
*{box-sizing:border-box;margin:0;padding:0}
html,body{width:1200px;height:945px;overflow:hidden}
body{background:var(--bg);font-family:"Open Sans",Arial,sans-serif;color:var(--ink);position:relative}
.sheet{position:absolute;background:var(--paper);box-shadow:0 4px 14px rgba(20,30,60,.18);overflow:hidden}
.wave{position:absolute;left:0;bottom:0;width:100%;display:block}
.brand{display:flex;align-items:center;gap:8px}
.brand-dot{width:30px;height:30px;border-radius:50%;background:var(--blue);flex:none}
.brand-name{font-weight:800;color:var(--navy);font-size:13px;line-height:1.15;text-transform:uppercase}
.contact{position:absolute;right:16px;bottom:10px;color:#fff;font-size:8.5px;line-height:1.45;text-align:right}

/* business cards */
.card{width:330px;height:188px}
.card-front{left:40px;top:40px}
.card-back{left:40px;top:252px}
.card .brand{position:absolute;left:18px;top:18px}
.card-person{position:absolute;right:18px;top:26px;text-align:right}
.card-person .name{font-weight:600;color:var(--red);font-size:12px}
.card-person .title{font-size:9.5px;color:var(--ink)}
.card-back .brand{left:50%;top:50px;transform:translateX(-50%)}
.card-back .brand-dot{width:44px;height:44px}
.card-back .brand-name{font-size:16px}
.card-back .web{position:absolute;left:0;right:0;bottom:12px;text-align:center;color:#fff;font-size:9px}

/* small card envelope */
.mini-env{left:40px;top:464px;width:330px;height:150px}
.mini-env .flap{position:absolute;right:0;top:0;height:100%;width:60px;border-left:1px solid var(--line);background:#f6f8fb}

/* letterhead */
.letterhead{left:400px;top:40px;width:360px;height:466px}
.letterhead .brand{position:absolute;left:22px;top:22px}
.watermark{position:absolute;left:50%;top:170px;transform:translateX(-50%);display:flex;flex-direction:column;align-items:center;gap:10px;opacity:.1}
.watermark .brand-dot{width:120px;height:120px}
.watermark .brand-name{font-size:24px;text-align:center}

/* fax */
.fax{left:790px;top:40px;width:360px;height:466px}
.fax .brand{position:absolute;left:22px;top:22px}
.fax-label{position:absolute;right:22px;top:28px;font-weight:800;color:var(--navy);font-size:22px;letter-spacing:2px}
.fax-table{position:absolute;left:22px;right:22px;top:84px;border-collapse:collapse;font-size:9px}
.fax-table td{border:1px solid var(--line);padding:5px 6px;width:25%}
.fax-table td.k{background:var(--navy);color:#fff;font-weight:600}

/* envelopes */
.env-front{left:40px;top:650px;width:470px;height:250px}
.env-front .brand{position:absolute;left:20px;top:18px}
.env-front .addr{position:absolute;left:60px;top:54px;font-size:8.5px;line-height:1.45}
.env-back{left:540px;width:610px;height:160px}
.env-red{top:560px}
.env-blue{top:740px}
.env-back svg{position:absolute;inset:0;width:100%;height:100%}
.seal{position:absolute;left:50%;top:70px;transform:translateX(-50%);background:#fff;border-radius:20px;padding:5px 12px;box-shadow:0 1px 4px rgba(0,0,0,.2)}
.seal .brand-dot{width:18px;height:18px}
.seal .brand-name{font-size:10px}
</style>
</head>
<body>

<section class="sheet card card-front">
  <div class="brand"><span class="brand-dot"></span><span class="brand-name">Sunny Harbor<br>Snackworks</span></div>
  <div class="card-person"><div class="name">Daniel T. Whitcombe</div><div class="title">Partner</div></div>
  <svg class="wave" height="80" viewBox="0 0 400 100" preserveAspectRatio="none"><path d="M0 30 C120 90 260 -10 400 20 L400 100 L0 100Z" fill="var(--sky)"/><path d="M0 44 C120 100 260 2 400 34 L400 100 L0 100Z" fill="var(--red)"/><path d="M0 52 C120 108 260 10 400 42 L400 100 L0 100Z" fill="var(--navy)"/></svg>
  <div class="contact">4870 Lakeview Court East · Morganville, NJ 07751<br>Tel 732.555.0148<br>dwhitcombe@sunnyharborsnackworks.com</div>
</section>

<section class="sheet card card-back">
  <div class="brand"><span class="brand-dot"></span><span class="brand-name">Sunny Harbor<br>Snackworks</span></div>
  <svg class="wave" height="52" viewBox="0 0 400 100" preserveAspectRatio="none"><path d="M0 30 C120 90 260 -10 400 20 L400 100 L0 100Z" fill="var(--sky)"/><path d="M0 44 C120 100 260 2 400 34 L400 100 L0 100Z" fill="var(--red)"/><path d="M0 52 C120 108 260 10 400 42 L400 100 L0 100Z" fill="var(--navy)"/></svg>
  <div class="web">sunnyharborsnackworks.com</div>
</section>

<section class="sheet mini-env">
  <div class="flap"></div>
  <svg class="wave" height="40" viewBox="0 0 400 100" preserveAspectRatio="none"><path d="M0 40 C120 100 260 0 400 30 L400 100 L0 100Z" fill="var(--red)"/><path d="M0 52 C120 108 260 10 400 42 L400 100 L0 100Z" fill="var(--navy)"/></svg>
</section>

<section class="sheet letterhead">
  <div class="brand"><span class="brand-dot"></span><span class="brand-name">Sunny Harbor<br>Snackworks</span></div>
  <div class="watermark"><span class="brand-dot"></span><span class="brand-name">Sunny Harbor<br>Snackworks</span></div>
  <svg class="wave" height="80" viewBox="0 0 400 100" preserveAspectRatio="none"><path d="M0 30 C120 90 260 -10 400 20 L400 100 L0 100Z" fill="var(--sky)"/><path d="M0 44 C120 100 260 2 400 34 L400 100 L0 100Z" fill="var(--red)"/><path d="M0 52 C120 108 260 10 400 42 L400 100 L0 100Z" fill="var(--navy)"/></svg>
  <div class="contact">Sunny Harbor Snackworks, LLC<br>4870 Lakeview Court East · Morganville, NJ 07751<br>sunnyharborsnackworks.com</div>
</section>

<section class="sheet fax">
  <div class="brand"><span class="brand-dot"></span><span class="brand-name">Sunny Harbor<br>Snackworks</span></div>
  <div class="fax-label">FAX</div>
  <table class="fax-table">
    <tr><td class="k">To</td><td></td><td class="k">From</td><td></td></tr>
    <tr><td class="k">Fax</td><td></td><td class="k">Date</td><td></td></tr>
    <tr><td class="k">Re</td><td></td><td class="k">Pages</td><td></td></tr>
  </table>
  <svg class="wave" height="80" viewBox="0 0 400 100" preserveAspectRatio="none"><path d="M0 30 C120 90 260 -10 400 20 L400 100 L0 100Z" fill="var(--sky)"/><path d="M0 44 C120 100 260 2 400 34 L400 100 L0 100Z" fill="var(--red)"/><path d="M0 52 C120 108 260 10 400 42 L400 100 L0 100Z" fill="var(--navy)"/></svg>
  <div class="contact">Tel 732.555.0148 · Fax 732.555.0149<br>sunnyharborsnackworks.com</div>
</section>

<section class="sheet env-front">
  <div class="brand"><span class="brand-dot"></span><span class="brand-name">Sunny Harbor<br>Snackworks</span></div>
  <div class="addr">4870 Lakeview Court East<br>Morganville, NJ 07751</div>
  <svg class="wave" height="90" viewBox="0 0 400 100" preserveAspectRatio="none"><path d="M0 30 C120 90 260 -10 400 20 L400 100 L0 100Z" fill="var(--sky)"/><path d="M0 44 C120 100 260 2 400 34 L400 100 L0 100Z" fill="var(--red)"/><path d="M0 52 C120 108 260 10 400 42 L400 100 L0 100Z" fill="var(--navy)"/></svg>
</section>

<section class="sheet env-back env-red">
  <svg viewBox="0 0 610 160" preserveAspectRatio="none"><path d="M0 0 L305 92 L610 0Z" fill="var(--red)"/><path d="M0 0 L305 92 L610 0" fill="none" stroke="#fff" stroke-width="3"/><path d="M0 160 L305 80 L610 160" fill="none" stroke="var(--line)"/></svg>
  <div class="seal brand"><span class="brand-dot"></span><span class="brand-name">Sunny Harbor Snackworks</span></div>
</section>

<section class="sheet env-back env-blue">
  <svg viewBox="0 0 610 160" preserveAspectRatio="none"><path d="M0 0 L305 92 L610 0Z" fill="var(--sky)"/><path d="M0 0 L305 92 L610 0" fill="none" stroke="#fff" stroke-width="3"/><path d="M0 160 L305 80 L610 160" fill="none" stroke="var(--line)"/></svg>
  <div class="seal brand"><span class="brand-dot"></span><span class="brand-name">Sunny Harbor Snackworks</span></div>
</section>

</body>
</html>
```